Dynamic Website Design For Dynamic Speaker and Business Coach!

Professional Website Design for a for a Professional Business coach, Business trainer, and Speaker.

Note: This is for design only. No coding required. We want to see your ideas for a great website! This will be a FUN design and not boring like others you may work on.

Please let your creative ideas flow. We have given you a ton of info along with videos to help you understand what we are after, however we WANT your creativity to shine through in your designs!

We are a professional company that has run hundreds of crowdsourced projects on multiple platforms. If you participate in this contest (we hope you do) you can expect great video feedback, consistent feedback, and also our guarantee that if we know your website design will not be what we are looking for we will notify you so you don’t waste your time if there is no chance of you winning.

We respect and recognize this is how you make your living and we will not play games. We look forward to an awesome contest and awesome website designs.

Design Brief:

We are looking for a fresh and fun new design for

http://www.grovepath7.net

This individual (Dana Wilcox) teaches and trains corporations and businesses in the fields of leadership, sales, communication, business operations etc. Additionally this business teaches and mentors business professionals in a small group level or 1 on 1.

The website needs to convey trust, professionalism, and affluent, while at the same time having some personality!

This business operates on 3 core principles that we would like to see incorporated into the logo if it is a good fit. The 3 principals are:

Focus
Accountability
Results

Here is a video to help explain what we like about the current site and what we don’t like:
http://clipvault.example/t/Qm7rTpLw2xKa

As you can see the website is geared towards business professionals. Please look over the website to learn what they do. Obviously this is not a good website so we need your help.

We want a website that is professional-looking, has personality and is geared more towards promoting Dana Wilcox, the owner of Grovepath 7 Partners as a Speaker and Business Consultant. The more you can incorporate clean, professional and fun personality elements into the design, the better off you are at winning.

Here are some examples of other sites in their business that have some things we like:

http://hemlineplays.example Please watch video to learn what we like and don’t like:
http://clipvault.example/t/NrpW3kTyvQa

http://tallpinepromo.example Please watch video to learn what we like and don’t like:
http://clipvault.example/t/K9wPzmRu

http://www.marlaquint.example Please watch video to learn what we like and don’t like:
http://clipvault.example/t/Vx2pq7N5a81

http://www.dwl7z.example Please watch video to learn what we like and don’t like:
http://clipvault.example/t/8K3wuhTzbnx

NOTE: We do not want to copy anything outright. We want to learn, model and take their ideas and make them better. We also want to be flexible and take what we like along with your creativity to make an amazing design.

Here is what we are looking for in more specific terms:

Colors: We like the darker blue (not the light blue like the site) and also a burnt orange. I’ve attached her Logo so you can get an idea and feel for the colors.

When looking at colors please know that the current site and look is NOT what we are going for. We are going for a clean and professional look but also a look that is BOLD, FUN, and Vibrant (hence the colors).

Menu: Horizontal. We like bold and easy to read menu items. Don’t make it small and cluttered.

Site Structure: Clean and easy to navigate. We have a lot of content to display so we need a clean structure that breaks up the text and content areas.
Images: Please pull images from the current site. We can always replace the images of course, but if you show them “their own stuff” in the new design you will be closer to winning because it will feel more like “them”

Look and Feel: Professional. Fun. High-End. Business-like. This website needs to convey that Dana Wilcox and Grovepath 7 Partners are professional. That Dana Wilcox is a sought-after Speaker and Business Consultant who knows what she is talking about; can be serious when she needs to be, but also likes to have fun with her clients. This site must convey that!

Content Areas: It is a safe bet that if it is on the current site we need it on the new site. So don’t drop anything as it makes it hard to “cut content”.

What we don't want: We do not want clutter, boring, or templates or themes. We don’t want too cartoony, too cute, or too fancy… Be creative!

Out of respect to professional designers who really are working hard to win if you do not follow this brief, you submit worn out themes, templates, or boring designs you will be eliminated. We are offering great prize money for this so we expect great visual designs.

Reason: Our client is out of town, and waiting to hear feedback from them. So, in the meantime, we wanted to keep the project going to see what else you designers can come up with. As soon as we hear back from our client, we will pass along the info. Thanks!

Target Market(s)

Target Audience is entrepreneurs and business professionals alike. This is all business to business stuff.

This person teaches and trains startups and billion dollar companies. The common thread is that they are all businesses and companies who need help in various areas including sales, communication, business operations, etc.

Industry/Entity Type

Business

Font styles to use
Sans Serif

Requirements
Must have
• Brief is very detailed. Please review
Nice to have
Should not have

```html
<!DOCTYPE html>
<html lang="en">
<head>
<meta charset="utf-8">
<title>Grovepath 7 Partners — Business Coaching</title>
<link href="https://fonts.googleapis.com/css2?family=Open+Sans:wght@400;600;700&display=swap" rel="stylesheet">
<style>
:root{
  --navy:#1f2a8a;
  --navy-deep:#1a2270;
  --orange:#e07a2a;
  --ink:#3a3a3a;
  --muted:#6b6b6b;
  --grey-bg:#ececec;
  --line:#c9c9c9;
  --white:#ffffff;
}
*{box-sizing:border-box;margin:0;padding:0}
html,body{width:1200px;height:2831px;overflow:hidden}
body{font-family:"Open Sans",Arial,sans-serif;color:var(--ink);background:var(--white);position:relative}
.abs{position:absolute}
ul{list-style:none}
h2,h3{font-weight:400}

/* top bar */
.topbar{left:0;top:0;width:1200px;height:40px;background:#f4f4f4;border-bottom:1px solid #e2e2e2}
.topbar .phone{left:116px;top:8px;font-size:15px;color:var(--muted);display:flex;align-items:center;gap:10px}
.topbar .phone-icon{width:20px;height:20px;background:var(--orange);border-radius:3px;display:flex;align-items:center;justify-content:center}
.topbar .follow{right:110px;top:7px;display:flex;align-items:center;gap:10px;font-size:15px;font-weight:700;color:var(--orange)}
.social-square{width:22px;height:22px;background:#7a7f86;border-radius:3px}

/* header */
.brand{left:112px;top:56px;display:flex;align-items:center;gap:14px}
.brand-mark{width:62px;height:62px;border-radius:50%;background:var(--orange)}
.brand-name{font-size:36px;font-weight:700;color:var(--navy);line-height:1}
.search{left:904px;top:102px;width:186px;height:36px;display:flex}
.search span{flex:1;background:#e4e4e4;font-size:13px;color:#9a9a9a;padding:9px 20px}
.search i{width:36px;background:#8a8a8a;display:flex;align-items:center;justify-content:center}

/* nav */
.mainnav{left:0;top:154px;width:1200px;height:52px;background:var(--navy);display:flex;align-items:center;padding-left:104px}
.nav-home{width:42px;height:40px;background:#2a78c0;display:flex;align-items:center;justify-content:center;margin-right:10px}
.mainnav a{color:var(--white);font-size:15px;font-weight:700;text-decoration:none;padding:0 14px;height:52px;display:flex;align-items:center}
.mainnav a.active{background:var(--orange);padding:0 22px}

/* hero */
.hero{left:0;top:206px;width:1200px;height:500px;background:linear-gradient(100deg,#c9ccd2 0%,#e9ebee 35%,#f3f3f3 55%,#9aa2b3 80%,#4c5570 100%)}
.hero-tag{background:var(--navy);color:var(--white);font-weight:700;position:absolute;left:372px;padding:0 18px;display:flex;align-items:center;border-right:6px solid var(--orange)}
.hero-tag.l1{top:280px;height:72px;width:466px;font-size:56px}
.hero-tag.l2{top:366px;height:70px;width:464px;font-size:56px}
.hero-tag.l3{top:448px;height:76px;width:468px;font-size:32px}
.btn-hero{left:518px;top:588px;width:154px;height:56px;background:var(--navy-deep);color:var(--white);font-size:21px;font-weight:700;border-radius:4px;display:flex;align-items:center;justify-content:center}

/* section headings */
.sec-title{left:0;width:1200px;text-align:center;font-size:30px;font-weight:400;color:#333;text-transform:uppercase;letter-spacing:.5px}
.sec-sub{left:0;width:1200px;text-align:center;font-size:20px;color:#444}
.divider{left:432px;width:336px;height:2px;background:var(--line)}
.divider::after{content:"";position:absolute;left:138px;top:-2px;width:60px;height:6px;background:var(--orange)}

.intro{left:190px;top:836px;width:820px;text-align:center;font-size:14.5px;line-height:25px;color:#555}

/* pillars */
.pillar{top:964px;width:256px;height:124px;border:2px solid var(--navy);background:var(--white);padding:16px 20px 0 32px}
.pillar.focus{border-color:var(--orange)}
.pillar h3{font-size:18px;font-weight:700;color:#333;text-transform:uppercase;margin-bottom:6px}
.pillar p{font-size:12.5px;line-height:20px;color:#666}
.pillar-icon{position:absolute;left:-36px;top:-6px;width:54px;height:54px;border-radius:50%;background:var(--navy);border:4px solid var(--white);box-shadow:0 0 0 2px var(--navy);display:flex;align-items:center;justify-content:center}

/* features */
.features{left:0;top:1144px;width:1200px;height:480px;background:var(--grey-bg)}
.video{left:104px;top:1300px;width:510px;height:288px;border:4px solid var(--orange);background:linear-gradient(135deg,#1f5c94,#2f86c6 55%,#1a4f82)}
.video-bar{position:absolute;left:0;bottom:0;width:100%;height:32px;background:rgba(10,20,40,.75);display:flex;align-items:center;gap:14px;padding:0 14px}
.video-track{flex:1;height:6px;background:#6d7788}
.feat-text{left:644px;top:1302px;width:460px;font-size:14px;line-height:26px;color:#444}
.arrow-list li{font-size:13.5px;line-height:26px;color:#444;padding-left:18px;position:relative}
.arrow-list li::before{content:"»";position:absolute;left:0;color:#777}
.feat-list{left:644px;top:1374px}
.btn-orange{top:1534px;height:40px;background:var(--orange);color:var(--white);font-size:15px;font-weight:700;display:flex;align-items:center;justify-content:center}

/* clients learn */
.learn-text{left:120px;top:1740px;width:660px;font-size:13.5px;line-height:26px;color:#444}
.learn-list{left:120px;top:1890px}
.illustration{left:810px;top:1756px;width:256px;height:300px;border-radius:8px;background:radial-gradient(circle at 55% 55%,#f6d24a 0,#f0c23a 22%,#e9e9e9 23%,#f4f4f4 70%)}

/* testimonials */
.testimonials{left:0;top:2090px;width:1200px;height:374px;background:linear-gradient(180deg,#3a3a3a,#262626 60%,#1d1d1d)}
.testimonials .sec-title{color:var(--white);top:34px}
.testimonials .divider{top:84px}
.avatar{left:546px;top:110px;width:102px;height:102px;border:4px solid var(--orange);background:linear-gradient(180deg,#e9d9c8,#c7a98c)}
.quote{left:150px;top:226px;width:900px;text-align:center;font-size:13.5px;line-height:22px;color:#e8e8e8}
.dots{left:570px;top:330px;display:flex;gap:8px}
.dots span{width:14px;height:14px;background:var(--white)}
.dots span.on{background:var(--orange)}

/* words & signup */
.contact-band{left:0;top:2464px;width:1200px;height:306px;background:linear-gradient(180deg,#27329a,#1e2a86)}
.band-title{font-size:21px;font-weight:400;color:var(--white)}
.words-quote{left:110px;top:2530px;width:486px;height:92px;padding:14px 10px 0 10px;font-size:12.5px;line-height:22px;color:#e6e8f5}
.corner{position:absolute;width:24px;height:24px;border-color:#aab0d8;border-style:solid}
.corner.tl{left:0;top:0;border-width:3px 0 0 3px}
.corner.br{right:0;bottom:0;border-width:0 3px 3px 0}
.portrait{left:124px;top:2634px;width:108px;height:108px;border:3px solid var(--orange);background:linear-gradient(180deg,#c9a58a,#7c5a4a)}
.vrule{left:626px;top:2500px;width:1px;height:250px;background:#5a64b8}
.signup-text{left:650px;top:2538px;font-size:15px;line-height:28px;color:var(--white)}
.signup-text em{font-style:normal;color:#f2722e}
.field{left:654px;width:238px;height:36px;background:#3a48b8;color:#c8cdf0;font-size:14px;padding:8px 22px}
.btn-submit{left:912px;top:2696px;width:80px;height:36px;background:var(--orange);color:var(--white);font-size:14px;display:flex;align-items:center;justify-content:center}

/* footer nav */
.footnav{left:0;top:2770px;width:1200px;height:61px;background:var(--orange);display:flex;align-items:center;justify-content:center;gap:30px}
.footnav a{color:var(--white);font-weight:700;font-size:15px;text-decoration:none}
</style>
</head>
<body>

<div class="abs topbar">
  <div class="abs phone">
    <span class="phone-icon"><svg width="12" height="12" viewBox="0 0 24 24"><path fill="#fff" d="M6.6 10.8a15 15 0 0 0 6.6 6.6l2.2-2.2a1 1 0 0 1 1-.25 11.4 11.4 0 0 0 3.6.57 1 1 0 0 1 1 1V20a1 1 0 0 1-1 1A17 17 0 0 1 3 4a1 1 0 0 1 1-1h3.5a1 1 0 0 1 1 1c0 1.25.2 2.45.57 3.57a1 1 0 0 1-.25 1z"/></svg></span>
    (555) 014-2290
  </div>
  <div class="abs follow">Follow Me : <span class="social-square"></span><span class="social-square"></span><span class="social-square"></span></div>
</div>

<div class="abs brand">
  <span class="brand-mark"></span>
  <span class="brand-name">Grovepath 7 Partners</span>
</div>
<div class="abs search">
  <span>Search</span>
  <i><svg width="14" height="14" viewBox="0 0 24 24"><circle cx="10" cy="10" r="6" fill="none" stroke="#fff" stroke-width="3"/><path d="M15 15l6 6" stroke="#fff" stroke-width="3"/></svg></i>
</div>

<nav class="abs mainnav">
  <span class="nav-home"><svg width="22" height="20" viewBox="0 0 24 22"><path fill="#fff" d="M12 1 1 11h3v10h6v-6h4v6h6V11h3z"/></svg></span>
  <a class="active">Passion</a><a>Who We Are?</a><a>Speaker</a><a>Free Video</a><a>Web TV Show</a><a>Testimonials</a><a>Harlow Learning</a><a>Blog</a><a>Contact</a>
</nav>

<section class="abs hero" role="img" aria-label="Photo of smiling business professionals around a meeting table"></section>
<div class="hero-tag l1">Do You Need</div>
<div class="hero-tag l2">More Focus,</div>
<div class="hero-tag l3">Accountaibility &amp; Results?</div>
<div class="abs btn-hero">Learn More</div>

<h2 class="abs sec-title" style="top:732px">How We Work</h2>
<p class="abs sec-sub" style="top:778px">Cedarmont Business Coaching and Consulting</p>
<div class="abs divider" style="top:820px"></div>
<p class="abs intro">Are you searching to bridge the gap between where you are and where you want to be?<br>As you face greater pressure to “move the needle” on your company’s productivity and bottom line profitability, how prepared are you to step in and shine as the leader?</p>

<div class="abs pillar focus" style="left:150px">
  <span class="pillar-icon"><svg width="22" height="22" viewBox="0 0 24 24"><path fill="#fff" d="M2 11 22 2l-9 20-2-9z"/></svg></span>
  <h3>Focus</h3><p>Morbi tristique, odio vitae elementum facilisis, nibh turpis blandit ipsum, vitae sagittis orci.</p>
</div>
<div class="abs pillar" style="left:480px">
  <span class="pillar-icon"><svg width="22" height="18" viewBox="0 0 24 18"><rect x="1" y="1" width="22" height="16" rx="2" fill="none" stroke="#fff" stroke-width="2"/><rect x="1" y="5" width="22" height="3" fill="#fff"/></svg></span>
  <h3>Accountabilty</h3><p>Morbi tristique, odio vitae elementum facilisis, nibh turpis blandit ipsum, vitae sagittis orci.</p>
</div>
<div class="abs pillar" style="left:812px">
  <span class="pillar-icon"><svg width="22" height="22" viewBox="0 0 24 24"><path fill="#fff" d="M2 10h4v12H2zM8 22h10a2 2 0 0 0 2-1.6l2-8A2 2 0 0 0 20 10h-6l1-5a2 2 0 0 0-3.6-1.4L8 9z"/></svg></span>
  <h3>Results</h3><p>Morbi tristique, odio vitae elementum facilisis, nibh turpis blandit ipsum, vitae sagittis orci.</p>
</div>

<section class="abs features"></section>
<h2 class="abs sec-title" style="top:1168px">Features</h2>
<p class="abs sec-sub" style="top:1212px">Your organization expects you to deliver value by delivering results.</p>
<div class="abs divider" style="top:1256px"></div>
<div class="abs video" role="img" aria-label="Video still of the coach presenting beside the headline on a blue background">
  <div class="video-bar">
    <svg width="14" height="16" viewBox="0 0 14 16"><path fill="#fff" d="M0 0l14 8-14 8z"/></svg>
    <span class="video-track"></span>
  </div>
</div>
<p class="abs feat-text">We specialize in guiding leaders to become easier to follow.&nbsp; You’re in the Right Place.</p>
<ul class="abs arrow-list feat-list">
  <li>Development Of An Operational Plan That Links All Departments</li>
  <li>Implementation And Monitoring Individual And Departmental Plans</li>
  <li>Diagnosing Employee Training Needs</li>
  <li>Delivering The Training To Develop Leaders And Staff</li>
  <li>Coach Leaders, Individuals And Teams</li>
</ul>
<div class="abs btn-orange" style="left:644px;width:118px">Web TV Show</div>
<div class="abs btn-orange" style="left:778px;width:116px">Free Videos</div>

<h2 class="abs sec-title" style="top:1636px">Our Clients Learn To</h2>
<p class="abs sec-sub" style="top:1676px">Grovepath 7 Partners has delivered on our promise</p>
<div class="abs divider" style="top:1716px"></div>
<p class="abs learn-text">At Grovepath 7 Partners, we know as a company or as individuals, clarity of the direction captured in an annual plan that is monitored monthly is one of the surest, quickest and most profitable ways of getting ahead in these challenging times.<br>What is the missing link in your business?&nbsp; What are you searching for?&nbsp; Email me today, conversation is complimentary to investigate where we start building&nbsp; the business you envision for tomorrow.</p>
<ul class="abs arrow-list learn-list">
  <li>Establish new patterns of productivity for the business</li>
  <li>Clarification of future goals, targets and benchmarks</li>
  <li>Implement actionable steps around short, medium and long-term goals</li>
  <li>Identify roadblocks and disempowering habits</li>
  <li>Create a repeatable process that delivers results</li>
  <li>Transform burned out employees or leaders into fired-up employees</li>
</ul>
<div class="abs illustration" role="img" aria-label="Illustration of a white figure leaning on a yellow clipboard checklist"></div>

<section class="abs testimonials" role="img" aria-label="Dark photo of a business handshake behind the testimonial">
  <h2 class="abs sec-title">What Our Clients Say About Us</h2>
  <div class="abs divider"></div>
  <div class="abs avatar" role="img" aria-label="Client portrait"></div>
  <p class="abs quote">“I don’t know a single person in Cedarmont who can network like Dana Wilcox. She is truly in a league of her own with respect to making human connections. Every time I attend one of her seminars, I get valuable information for running my business and I notice that Dana goes out of her way to help the attendees find synergies with each other for future business and development. I would recommend that everyone in business give Dana the opportunity to show them how valuable she can be to their organization.”</p>
  <div class="abs dots"><span class="on"></span><span></span><span></span></div>
</section>

<section class="abs contact-band"></section>
<h3 class="abs band-title" style="left:118px;top:2486px">Words From :</h3>
<div class="abs words-quote">
  <span class="corner tl"></span><span class="corner br"></span>
  With over 25 years of experience in a variety of industries, we know the daily attitudes, habits and goals for successful companies begin with a plan. By training employees where needed and coaching to clear expectations writes success stories daily as the plan unfolds over the course of the year.
</div>
<div class="abs portrait" role="img" aria-label="Portrait of Dana Wilcox"></div>
<p class="abs" style="left:256px;top:2684px;font-size:13px;color:#fff">Here’s to your success!</p>
<p class="abs" style="left:256px;top:2714px;font-size:19px;color:#fff">Dana Wilcox</p>
<div class="abs vrule"></div>
<h3 class="abs band-title" style="left:650px;top:2486px">Sign Up :</h3>
<p class="abs signup-text">Change your thinking, change your results!<br>Sign up for my FREE report <em>“Smile While You Close Deals”</em><br>and make more money this month!</p>
<div class="abs field" style="top:2644px">E-mail</div>
<div class="abs field" style="top:2696px">Name</div>
<div class="abs btn-submit">Submit</div>

<nav class="abs footnav">
  <a>Home</a><a>Passion</a><a>Who We Are?</a><a>Speaker</a><a>Free Video</a><a>Web TV Show</a><a>Testimonials</a><a>Harlow Learning</a><a>Blog</a><a>Contact</a>
</nav>

</body>
</html>
```